Car wrap for landscaping/gardening company (in Portuguese)

This is a landscaping company that is fully electric, providing, silent, emissions-free landscaping to the community. I am requesting a wrap for the residential van that will be used for this service.

The key things that the wrap must convey, besides the logo of the company, is:
(1) 100% electric (100% Elétrico)
(2) Silent (Silencioso)
(3) No emissions (Sem Emissões)
I envision three large, round icons with a simple image illustrating each of these concepts, and below each icon the text in Portuguese. The van only has to have the logo and the icons, plus a space for phone number and website which can be a little smaller. Use bold colors, make it modern. Don't make it flowery, that will not distinguish the van.

An additional icon can also be added for Customer Service. So possibly 4 icons, with the 4th one saying "Serviço ao Cliente." I am interested in seeing alternatives with 3 and 4 icons.

Please check out the sample that I sent. I like this wrap because it is simple and very visible. It has a lot of text in the rear though which is difficult to read. I don't want this kind of text. Just the icons and the titles. Make it super clear.

The service is high tech, innovative, and premium. It is not a normal landscaping company. I want to attract high end customers who demand the best, who want landscaping that is silent and clean for the environment.

Target Market(s)

Residential customers with patios, large houses, looking for high tech landscaping service and willing to pay a premium

Industry/Entity Type

Landscaping, Gardening

Font styles to use
Sans Serif

Requirements
Must have
• Please use the logo that I have provided. I also need three icons, well displayed, each one representing an aspect of our service: (1) 100% ELÉTRICO (2) SILENCIOSO (3) SEM EMISSÕES. In Portuguese it means 100% electric, Silent, No emissions. Can be three round icons below the logo, very prominent so that people know what the service is about. Also need a place to put two phone numbers, on the back and on the door, as well as the website.
Nice to have
• The picture that I showed is a good example of a blue car wrap. This can work but has to be in green or brown (landscaping colors). I like it because it is bold and visible, and doesn't have too many decorative features. It is very modern and simple, which is consistent with the theme that I am looking for.
Should not have
• Flowery shapes, too much decoration, curvy lines, excessive text

```html
<!DOCTYPE html>
<html lang="pt">
<head>
<meta charset="utf-8">
<title>Verde Quieto – Van Wrap</title>
<link rel="stylesheet" href="https://fonts.googleapis.com/css2?family=Open+Sans:wght@400;700&display=swap">
<style>
  :root{
    --page:#f6f6f6;
    --wrap-green:#0f6e1e;
    --wrap-green-dark:#075414;
    --wrap-white:#ffffff;
    --edge:#111111;
    --brand-green:#1c8a2c;
    --ink-light:#ffffff;
  }
  html,body{margin:0;padding:0;width:1200px;height:1181px;overflow:hidden;background:var(--page);}
  .canvas{position:relative;width:1200px;height:1181px;}
  .panel{position:absolute;display:block;}
  .panel--side{left:150px;top:170px;}
  .panel--rear{left:360px;top:640px;}
  .wrap-text{font-family:"Open Sans",sans-serif;fill:var(--ink-light);font-weight:700;}
  .wrap-text--web{font-size:17px;}
  .wrap-text--phone{font-size:20px;}
  .brand-name{font-family:"Open Sans",sans-serif;font-weight:400;letter-spacing:1px;}
  .brand-name--side{fill:var(--brand-green);font-size:34px;}
  .brand-name--rear{fill:var(--ink-light);font-size:30px;}
  .icon-ring{fill:none;stroke:var(--ink-light);stroke-width:4;}
  .icon-line{fill:none;stroke:var(--ink-light);stroke-width:3.5;stroke-linecap:round;stroke-linejoin:round;}
  .icon-fill{fill:var(--ink-light);}
  .icon-badge{font-family:"Open Sans",sans-serif;font-weight:700;font-size:12px;fill:var(--ink-light);}
  .icon-title{font-family:"Open Sans",sans-serif;font-weight:700;font-size:10.5px;letter-spacing:.3px;fill:var(--ink-light);}
</style>
</head>
<body>
<main class="canvas">
  <svg width="0" height="0" style="position:absolute">
    <defs>
      <linearGradient id="greenField" x1="0" y1="0" x2="1" y2="1">
        <stop offset="0" stop-color="#13782a"/>
        <stop offset="1" stop-color="#075414"/>
      </linearGradient>
      <g id="icon-electric">
        <circle class="icon-ring" cx="0" cy="0" r="36"/>
        <path class="icon-fill" d="M4,-26 L-12,2 L-2,2 L-6,16 L12,-8 L2,-8 L8,-26 Z"/>
        <text class="icon-badge" x="0" y="29" text-anchor="middle">100%</text>
        <text class="icon-title" x="0" y="54" text-anchor="middle">100% ELÉTRICO</text>
      </g>
      <g id="icon-emissions">
        <circle class="icon-ring" cx="0" cy="0" r="36"/>
        <path class="icon-line" d="M-18,14 H18 A10,10 0 0 0 16,-6 A14,14 0 0 0 -10,-10 A11,11 0 0 0 -18,14 Z"/>
        <line class="icon-line" x1="-22" y1="-22" x2="22" y2="22"/>
        <text class="icon-title" x="0" y="54" text-anchor="middle">SEM EMISSÕES</text>
      </g>
      <g id="icon-silent">
        <circle class="icon-ring" cx="0" cy="0" r="36"/>
        <path class="icon-fill" d="M-22,-6 H-12 L4,-18 V18 L-12,6 H-22 Z"/>
        <path class="icon-line" d="M10,-8 Q15,0 10,8 M15,-13 Q23,0 15,13 M20,-18 Q30,0 20,18"/>
        <line class="icon-line" x1="-22" y1="-22" x2="22" y2="22"/>
        <text class="icon-title" x="0" y="54" text-anchor="middle">SILENCIOSO</text>
      </g>
    </defs>
  </svg>

  <svg class="panel panel--side" width="900" height="300" viewBox="0 0 900 300" aria-label="Verde Quieto side wrap">
    <rect x="0" y="0" width="900" height="300" fill="var(--wrap-white)"/>
    <polygon points="0,0 400,0 250,300 0,300" fill="url(#greenField)" role="img" aria-label="Green field with a faint scattered leaf pattern"/>
    <line x1="400" y1="0" x2="250" y2="300" stroke="var(--edge)" stroke-width="6"/>
    <use href="#icon-electric" x="70" y="66"/>
    <use href="#icon-emissions" x="160" y="66"/>
    <use href="#icon-silent" x="250" y="66"/>
    <text class="wrap-text wrap-text--web" x="172" y="172" text-anchor="middle">WWW.VERDEQUIETO.COM</text>
    <text class="wrap-text wrap-text--phone" x="172" y="198" text-anchor="middle">+44 800 31462750</text>
    <text class="brand-name brand-name--side" x="600" y="196" text-anchor="middle">VERDE QUIETO</text>
  </svg>

  <svg class="panel panel--rear" width="480" height="360" viewBox="0 0 480 360" aria-label="Verde Quieto rear wrap">
    <rect x="0" y="0" width="480" height="360" rx="18" fill="url(#greenField)" role="img" aria-label="Green field with a faint scattered leaf pattern"/>
    <use href="#icon-electric" x="150" y="62"/>
    <use href="#icon-emissions" x="240" y="62"/>
    <use href="#icon-silent" x="330" y="62"/>
    <text class="wrap-text wrap-text--web" x="240" y="164" text-anchor="middle">WWW.VERDEQUIETO.COM</text>
    <text class="wrap-text wrap-text--phone" x="240" y="191" text-anchor="middle">+44 800 31462750</text>
    <text class="brand-name brand-name--rear" x="240" y="266" text-anchor="middle">VERDE QUIETO</text>
  </svg>
</main>
</body>
</html>
```